Media/PR business needs a website upgrade

Modernise my website www.vrl.net.au into a simpler and mobile friendly site with the usual plugins, maximum 5 pages, 4 might be enough. My page is already hosted and I have an email address so I just want to work with a designer who is fantastic with WordPress, to refresh and simplify the 6 year-old look.

Target Market(s)

men & women 25-55

Industry/Entity Type

Business

Coding

Coded - Design and coding required

Number of Pages Required

4 page

Font styles to use
Sans Serif

Colors
f37122
ffffff

Requirements
Must have
• Social media plugins, about, client portfolio, contact (can be under about)blog capability
Nice to have
• photos of jobs I've done
Should not have
• e-commerce, can lose all the client logos

```html
<!DOCTYPE html>
<html lang="en">
<head>
<meta charset="utf-8">
<title>Vantage Relay Media</title>
<link href="https://fonts.googleapis.com/css2?family=Open+Sans:wght@400;600;700&family=Raleway:wght@400;500;600;700;800&display=swap" rel="stylesheet">
<style>
:root{
  --orange:#f37122;
  --white:#ffffff;
  --ink:#222222;
  --body:#666666;
  --line:#e4e4e4;
  --panel:#f5f5f5;
  --footer:#252525;
}
*{box-sizing:border-box;margin:0;padding:0}
html,body{width:1200px;height:3279px;overflow:hidden}
body{font-family:"Open Sans",sans-serif;color:var(--body);background:var(--white);position:relative}
.abs{position:absolute}
h2,h3,.nav,.brand{font-family:"Raleway",sans-serif}

/* header */
.header{left:0;top:0;width:1200px;height:116px;background:var(--white)}
.brand{left:131px;top:24px;display:flex;align-items:center;gap:10px}
.brand-dot{width:64px;height:64px;border-radius:50%;background:var(--orange)}
.brand-name{font-size:16px;font-weight:700;color:var(--ink);line-height:17px;width:150px}
.contact{top:20px;display:flex;align-items:center;gap:10px;font-size:12px;color:var(--ink)}
.contact b{font-size:15px;font-weight:600}
.contact-icon{width:32px;height:32px;border-radius:50%;background:var(--orange);display:flex;align-items:center;justify-content:center}
.nav{left:432px;top:74px;width:640px;display:flex;justify-content:space-between;font-size:12px;font-weight:600;color:var(--ink)}
.nav .active{color:var(--orange);border-bottom:2px solid var(--orange);padding-bottom:8px}

/* hero */
.hero{left:0;top:116px;width:1200px;height:501px;background:linear-gradient(90deg,#d9d2c9 0%,#e3ddd4 45%,#e8e3dc 100%)}
.hero-person{left:150px;top:116px;width:500px;height:501px;background:linear-gradient(180deg,#c79a76 0%,#b5896a 30%,#2f7fc6 62%,#d9d9d9 100%);opacity:.55}
.hero-title{left:560px;top:210px;width:550px;text-align:center;font-family:"Raleway",sans-serif;font-weight:800;font-size:50px;line-height:72px;color:var(--ink)}
.btn{display:inline-block;background:var(--orange);color:var(--white);border-radius:22px;font-size:13px;font-weight:600;text-align:center}
.hero-btn{left:754px;top:376px;width:162px;height:40px;line-height:40px}
.signature{left:750px;top:455px;width:170px;height:46px;background:linear-gradient(90deg,rgba(34,34,34,.12),rgba(34,34,34,.05))}
.arrow{width:48px;height:48px;border:2px solid #555;border-radius:50%;display:flex;align-items:center;justify-content:center}

/* services */
.section-title{left:0;width:1200px;text-align:center;font-size:25px;font-weight:700;color:var(--ink)}
.services{left:133px;top:804px;width:932px;height:208px;border:1px solid var(--line);display:flex}
.service{flex:1;border-right:1px solid var(--line);text-align:center;padding:66px 18px 0}
.service:last-child{border-right:0}
.service h3{font-size:14px;font-weight:700;color:var(--ink);margin-bottom:8px}
.service p{font-size:11px;line-height:21px}
.more{color:var(--orange);font-size:11px;font-weight:700;margin-top:7px;display:block}
.service-icon{width:88px;height:88px;border-radius:50%;background:var(--orange);top:756px;display:flex;align-items:center;justify-content:center}
.side-arrow{width:30px;height:30px;border-radius:50%;background:#bbb;top:892px;display:flex;align-items:center;justify-content:center}

/* about */
.about{left:0;top:1097px;width:599px;height:418px;background:var(--panel)}
.about h2{left:133px;top:1160px;font-size:26px;font-weight:700;color:var(--ink)}
.about-text{left:133px;top:1210px;width:420px;font-size:11px;line-height:21px}
.about-btn{left:133px;top:1374px;width:132px;height:38px;line-height:38px}
.photo{display:block}
.skills{left:133px;top:1493px;width:932px;height:350px;background:var(--white);border:1px solid var(--line);display:flex}
.skill-col{flex:1;padding:34px 38px}
.skill-col+.skill-col{border-left:1px solid var(--line)}
.skill-col h3{font-size:23px;font-weight:500;color:var(--ink);margin-bottom:14px}
.skill-col li{list-style:none;font-size:11px;line-height:24px;display:flex;align-items:center;gap:8px}

/* gallery */
.gallery{left:0;top:1926px;width:1200px;height:758px;background:var(--orange)}
.gallery-title{color:var(--white)}
.gal{border:2px solid rgba(255,255,255,.7)}

/* blog */
.post{top:2822px;width:293px;height:271px;border:1px solid var(--line);background:var(--white)}
.post-img{height:172px;position:relative}
.date{position:absolute;right:12px;top:0;width:56px;height:84px;background:var(--orange);color:var(--white);text-align:center;font-family:"Raleway",sans-serif}
.date b{display:block;font-size:26px;font-weight:600;padding-top:12px}
.date span{font-size:11px}
.post h3{font-size:14px;font-weight:500;color:var(--ink);padding:14px 12px 6px}
.post p{font-size:11px;line-height:20px;padding:0 12px}

/* footer */
.footer{left:0;top:3165px;width:1200px;height:114px;background:var(--footer);color:#ddd}
.footer-links{left:131px;top:3198px;font-size:10px;letter-spacing:.3px}
.copy{left:131px;top:3228px;font-size:10px}
.follow{left:850px;top:3206px;display:flex;align-items:center;gap:6px;font-size:11px}
.social{width:28px;height:28px;border-radius:50%;border:2px solid #ddd}
</style>
</head>
<body>

<header class="header abs"></header>
<div class="brand abs"><span class="brand-dot"></span><span class="brand-name">Vantage Relay Media</span></div>
<div class="contact abs" style="left:666px">
  <span class="contact-icon"><svg width="16" height="16" viewBox="0 0 24 24"><path fill="#fff" d="M6.6 10.8a15 15 0 006.6 6.6l2.2-2.2c.3-.3.7-.4 1-.2 1.1.4 2.3.6 3.6.6.6 0 1 .4 1 1V20c0 .6-.4 1-1 1A17 17 0 013 4c0-.6.4-1 1-1h3.5c.6 0 1 .4 1 1 0 1.3.2 2.5.6 3.6.1.3 0 .7-.2 1z"/></svg></span>
  <span>Contact : <b>0400 555 270</b></span>
</div>
<div class="contact abs" style="left:876px">
  <span class="contact-icon"><svg width="16" height="14" viewBox="0 0 24 20"><rect x="1" y="2" width="22" height="16" rx="2" fill="#fff"/><path d="M2 4l10 7 10-7" stroke="#f37122" stroke-width="2" fill="none"/></svg></span>
  <span>Email : <b>nora@vrl.net.au</b></span>
</div>
<nav class="nav abs"><span class="active">HOME</span><span>SERVICES</span><span>ABOUT</span><span>CLIENT</span><span>PORTFOLIO</span><span>TESTIMONIALS</span><span>BLOG</span><span>CONTACT</span></nav>

<section class="hero abs" role="img" aria-label="Backdrop of a light stone wall"></section>
<div class="hero-person abs" role="img" aria-label="Portrait of the founder in a blue shirt and grey sailing jacket"></div>
<h1 class="hero-title abs">VANTAGE<br>RELAY MEDIA</h1>
<span class="btn hero-btn abs">LEARN MORE INFO</span>
<div class="signature abs" role="img" aria-label="Handwritten signature of Nora Kemble"></div>
<span class="arrow abs" style="left:53px;top:343px"><svg width="12" height="16" viewBox="0 0 12 16"><path d="M9 2L3 8l6 6" stroke="#555" stroke-width="2" fill="none"/></svg></span>
<span class="arrow abs" style="left:1099px;top:343px"><svg width="12" height="16" viewBox="0 0 12 16"><path d="M3 2l6 6-6 6" stroke="#555" stroke-width="2" fill="none"/></svg></span>

<h2 class="section-title abs" style="top:692px">SERVICES</h2>
<div class="services abs">
  <div class="service"><h3>SPORTS MEDIA</h3><p>VRM founder Nora Kemble has worked closely with Australian and inter national sports media...</p><span class="more">READ MORE &gt;&gt;</span></div>
  <div class="service"><h3>PUBLICITY</h3><p>Generating media publicity for both the event and its sponsor is one of Nora's key strengths...</p><span class="more">READ MORE &gt;&gt;</span></div>
  <div class="service"><h3>SPONSORSHIP LEVERAGE</h3><p>Nora has worked with many sponsors including premium brand clients Meridian Watches and...</p><span class="more">READ MORE &gt;&gt;</span></div>
  <div class="service"><h3>EVENT MANAGEMENT</h3><p>From planning through to execution and follow up, VRM provides a complete service...</p><span class="more">READ MORE &gt;&gt;</span></div>
</div>
<span class="service-icon abs" style="left:206px"><svg width="44" height="44" viewBox="0 0 44 44"><circle cx="22" cy="22" r="19" fill="#fff"/><path d="M22 13l8 6-3 9h-10l-3-9z" fill="#f37122"/></svg></span>
<span class="service-icon abs" style="left:439px"><svg width="48" height="40" viewBox="0 0 48 40"><circle cx="24" cy="12" r="7" fill="#fff"/><path d="M12 36c0-8 5-13 12-13s12 5 12 13z" fill="#fff"/><circle cx="10" cy="15" r="5" fill="#fff"/><circle cx="38" cy="15" r="5" fill="#fff"/><path d="M1 33c0-6 4-10 9-10 2 0 3 .4 4 1-2 2-3 5-3 9zM47 33c0-6-4-10-9-10-2 0-3 .4-4 1 2 2 3 5 3 9z" fill="#fff"/></svg></span>
<span class="service-icon abs" style="left:672px"><svg width="44" height="44" viewBox="0 0 44 44"><path d="M12 6h20v10a10 10 0 01-20 0z" fill="#fff"/><path d="M12 9H5c0 7 4 10 8 10M32 9h7c0 7-4 10-8 10" stroke="#fff" stroke-width="3" fill="none"/><rect x="19" y="25" width="6" height="8" fill="#fff"/><rect x="13" y="33" width="18" height="5" fill="#fff"/><path d="M22 9l1.5 3 3 .4-2.2 2 .6 3-2.9-1.5-2.9 1.5.6-3-2.2-2 3-.4z" fill="#f37122"/></svg></span>
<span class="service-icon abs" style="left:905px"><svg width="42" height="42" viewBox="0 0 42 42"><rect x="4" y="7" width="34" height="31" rx="3" fill="#fff"/><rect x="4" y="7" width="34" height="8" fill="#fde3d2"/><rect x="11" y="3" width="4" height="9" rx="2" fill="#fff"/><rect x="27" y="3" width="4" height="9" rx="2" fill="#fff"/><text x="21" y="33" font-family="Raleway,sans-serif" font-size="16" font-weight="700" fill="#f37122" text-anchor="middle">25</text></svg></span>
<span class="side-arrow abs" style="left:94px"><svg width="10" height="12" viewBox="0 0 10 12"><path d="M7 1L2 6l5 5" stroke="#fff" stroke-width="2" fill="none"/></svg></span>
<span class="side-arrow abs" style="left:1074px"><svg width="10" height="12" viewBox="0 0 10 12"><path d="M3 1l5 5-5 5" stroke="#fff" stroke-width="2" fill="none"/></svg></span>

<section class="about abs"></section>
<h2 class="about abs" style="background:none;width:auto;height:auto;top:1160px;left:133px">ABOUT US</h2>
<div class="about-text abs">
  <p>An innovative and creative business owner with extensive experience from within the sporting industry. Offering expertise in a variety of areas including media relations, journalism and event management, I have successfully founded and built my own reputable public relations business.</p>
  <p style="margin-top:10px">With a proven track record in journalism and project management, along with a Bachelor in Communications...</p>
</div>
<span class="btn about-btn abs">LEARN MORE</span>
<div class="photo abs" style="left:600px;top:1097px;width:296px;height:418px;background:linear-gradient(180deg,#d8cfc3 0%,#c9a58a 30%,#3380c4 60%,#d8d8d8 100%)" role="img" aria-label="Founder standing against a stone wall in a sailing jacket"></div>
<div class="photo abs" style="left:901px;top:1097px;width:299px;height:206px;background:linear-gradient(180deg,#e2ddd5 0%,#c9a58a 55%,#cfcfcf 100%)" role="img" aria-label="Close portrait of the founder smiling"></div>
<div class="photo abs" style="left:901px;top:1307px;width:299px;height:208px;background:linear-gradient(180deg,#e2ddd5 0%,#c9a58a 50%,#3a85c8 100%)" role="img" aria-label="Portrait of the founder looking to camera"></div>

<div class="skills abs">
  <div class="skill-col"><h3>Technical Skills</h3><ul>
    <li><svg width="10" height="9"><path d="M1 5l3 3 5-7" stroke="#f37122" stroke-width="2" fill="none"/></svg>Media and Public Relations</li>
    <li><svg width="10" height="9"><path d="M1 5l3 3 5-7" stroke="#f37122" stroke-width="2" fill="none"/></svg>Project Management</li>
    <li><svg width="10" height="9"><path d="M1 5l3 3 5-7" stroke="#f37122" stroke-width="2" fill="none"/></svg>Communication Strategy Development</li>
    <li><svg width="10" height="9"><path d="M1 5l3 3 5-7" stroke="#f37122" stroke-width="2" fill="none"/></svg>Stakeholder Relationship Management</li>
    <li><svg width="10" height="9"><path d="M1 5l3 3 5-7" stroke="#f37122" stroke-width="2" fill="none"/></svg>Research and pitching story ideas and angles</li>
    <li><svg width="10" height="9"><path d="M1 5l3 3 5-7" stroke="#f37122" stroke-width="2" fill="none"/></svg>Maximising team performance</li>
    <li><svg width="10" height="9"><path d="M1 5l3 3 5-7" stroke="#f37122" stroke-width="2" fill="none"/></svg>Events management</li>
    <li><svg width="10" height="9"><path d="M1 5l3 3 5-7" stroke="#f37122" stroke-width="2" fill="none"/></svg>Sports journalism</li>
    <li><svg width="10" height="9"><path d="M1 5l3 3 5-7" stroke="#f37122" stroke-width="2" fill="none"/></svg>Interviewing clients, participants, athletes</li>
    <li><svg width="10" height="9"><path d="M1 5l3 3 5-7" stroke="#f37122" stroke-width="2" fill="none"/></svg>Copy writing/ creative writing</li>
  </ul></div>
  <div class="skill-col"><h3>Professional Skills</h3><ul>
    <li><svg width="10" height="9"><path d="M1 5l3 3 5-7" stroke="#f37122" stroke-width="2" fill="none"/></svg>Strong organisational skills</li>
    <li><svg width="10" height="9"><path d="M1 5l3 3 5-7" stroke="#f37122" stroke-width="2" fill="none"/></svg>Prioritizing and multitasking</li>
    <li><svg width="10" height="9"><path d="M1 5l3 3 5-7" stroke="#f37122" stroke-width="2" fill="none"/></svg>Ability to meet deadlines</li>
    <li><svg width="10" height="9"><path d="M1 5l3 3 5-7" stroke="#f37122" stroke-width="2" fill="none"/></svg>Excellent communication and interpersonal skills</li>
    <li><svg width="10" height="9"><path d="M1 5l3 3 5-7" stroke="#f37122" stroke-width="2" fill="none"/></svg>Results focused</li>
    <li><svg width="10" height="9"><path d="M1 5l3 3 5-7" stroke="#f37122" stroke-width="2" fill="none"/></svg>High level of initiative</li>
    <li><svg width="10" height="9"><path d="M1 5l3 3 5-7" stroke="#f37122" stroke-width="2" fill="none"/></svg>Ability to work both in a team and independently</li>
    <li><svg width="10" height="9"><path d="M1 5l3 3 5-7" stroke="#f37122" stroke-width="2" fill="none"/></svg>Impartial and trustworthy</li>
    <li><svg width="10" height="9"><path d="M1 5l3 3 5-7" stroke="#f37122" stroke-width="2" fill="none"/></svg>Creative and motivated</li>
    <li><svg width="10" height="9"><path d="M1 5l3 3 5-7" stroke="#f37122" stroke-width="2" fill="none"/></svg>Strong negotiation skills</li>
  </ul></div>
</div>

<section class="gallery abs"></section>
<h2 class="section-title gallery-title abs" style="top:1999px">PHOTO GALLERY</h2>
<div class="gal abs" style="left:133px;top:2072px;width:619px;height:258px;background:linear-gradient(160deg,#2a2420 0%,#7a5a3a 45%,#c9a070 70%,#3b3028 100%)" role="img" aria-label="Skiff sailors racing at sunset"></div>
<div class="gal abs" style="left:759px;top:2072px;width:308px;height:258px;background:linear-gradient(180deg,#9fb7d0 0%,#6d8fb2 45%,#2f5f95 70%,#d6e2ee 100%)" role="img" aria-label="Racing yacht heeling in harbour spray"></div>
<div class="gal abs" style="left:133px;top:2341px;width:306px;height:260px;background:linear-gradient(180deg,#86a8cf 0%,#5d7fa5 45%,#2e4766 100%)" role="img" aria-label="Crew gathered on a moored boat"></div>
<div class="gal abs" style="left:446px;top:2341px;width:306px;height:260px;background:linear-gradient(180deg,#7b9fc4 0%,#c9a58a 40%,#d8d8d8 70%,#c24030 100%)" role="img" aria-label="Founder on the water in a sailing jacket"></div>
<div class="gal abs" style="left:759px;top:2341px;width:308px;height:260px;background:linear-gradient(180deg,#4f90d8 0%,#7ab4e8 45%,#49b56a 60%,#2e6aa8 100%)" role="img" aria-label="Yacht flying a colourful spinnaker"></div>

<h2 class="section-title abs" style="top:2749px">LATEST BLOG</h2>
<article class="post abs" style="left:133px"><div class="post-img" style="background:linear-gradient(180deg,#3a4f7a 0%,#6a5a70 50%,#2a2a3a 100%)" role="img" aria-label="Group celebrating at an awards night"><div class="date"><b>12</b><span>OCT</span></div></div><h3>Excepteur sint occaecat cupidatat</h3><p>Eiusmod tempor incididunt ut labore et dolore magna aliqua aute irure dolor...</p></article>
<article class="post abs" style="left:455px"><div class="post-img" style="background:linear-gradient(180deg,#2b6ab0 0%,#c9a58a 50%,#e0c040 100%)" role="img" aria-label="Founder with an athlete at a media event"><div class="date"><b>13</b><span>OCT</span></div></div><h3>Excepteur sint occaecat cupidatat</h3><p>Eiusmod tempor incididunt ut labore et dolore magna aliqua aute irure dolor...</p></article>
<article class="post abs" style="left:776px"><div class="post-img" style="background:linear-gradient(180deg,#2a2a50 0%,#5a4a7a 50%,#1f1f2a 100%)" role="img" aria-label="Guests at an evening function"><div class="date"><b>14</b><span>OCT</span></div></div><h3>Excepteur sint occaecat cupidatat</h3><p>Eiusmod tempor incididunt ut labore et dolore magna aliqua aute irure dolor...</p></article>

<footer class="footer abs"></footer>
<div class="footer-links abs">HOME &nbsp;|&nbsp; SERVICES &nbsp;|&nbsp; ABOUT &nbsp;|&nbsp; CLIENT &nbsp;|&nbsp; PORTFOLIO &nbsp;|&nbsp; TESTIMONIALS &nbsp;|&nbsp; BLOG &nbsp;|&nbsp; CONTACT</div>
<div class="copy abs">COPYRIGHTS © 2017 , VANTAGE RELAY MEDIA | ALL RIGHTS RESERVED.</div>
<div class="follow abs"><span>FOLLOW US :</span><span class="social"></span><span class="social"></span><span class="social"></span><span class="social"></span><span class="social"></span></div>

</body>
</html>
```